R. Vantello needs an original business card for property investment professionals

The business card would be to present me as an investor in the real estate business. The market are developers of real estate projects, or other people who would like to sell and also to give us a name as a company. For style, colour and imagery I would like something artistic from Vantello (the artist) with a different touch.

Address, email, cel phone,
Updates

Hi¡ Update¡ I;d like it to stop providing Bright Ledger as a Design and focus in R.Vantello.

Target Market(s)

Real Estate Developer/Investor

Industry/Entity Type

Real Estate

Colors
33a6d7
886aae
e3daeb
cadf82
f78f20

```html
<!DOCTYPE html>
<html lang="en">
<head>
<meta charset="utf-8">
<title>R. Vantello – Business Card</title>
<link href="https://fonts.googleapis.com/css2?family=Quicksand:wght@500;600&display=swap" rel="stylesheet">
<style>
  :root {
    --blue: #33a6d7;
    --purple: #886aae;
    --lavender: #e3daeb;
    --green: #cadf82;
    --orange: #f78f20;
    --ink: #3a3a3a;
    --card: #ffffff;
    --stage: #ecebee;
  }
  * { box-sizing: border-box; margin: 0; padding: 0; }
  html, body {
    width: 1200px;
    height: 872px;
    overflow: hidden;
    background: var(--stage);
    font-family: "Quicksand", sans-serif;
  }
  .sheet {
    width: 1200px;
    height: 872px;
    display: flex;
    align-items: center;
    justify-content: center;
    gap: 90px;
  }
  .card {
    width: 340px;
    height: 560px;
    background: var(--card);
    border-radius: 4px;
    box-shadow: 0 10px 30px rgba(0,0,0,0.12), 0 2px 4px rgba(0,0,0,0.08);
    position: relative;
  }
  .brand {
    display: flex;
    align-items: center;
    justify-content: center;
    gap: 12px;
  }
  .brand-mark {
    width: 22px;
    height: 22px;
    background: var(--orange);
  }
  .brand-name {
    font-weight: 600;
    font-size: 40px;
    color: var(--blue);
    letter-spacing: 0.5px;
  }
  .card-front .brand { margin-top: 120px; }
  .tagline {
    margin-top: 8px;
    text-align: center;
    font-weight: 500;
    font-size: 13px;
    letter-spacing: 1.6px;
    color: var(--purple);
  }
  .tagline-rule {
    display: block;
    width: 190px;
    height: 2px;
    margin: 10px auto 0;
    background: var(--blue);
    border-radius: 2px;
  }
  .contact-list {
    position: absolute;
    left: 150px;
    top: 360px;
    list-style: none;
  }
  .contact-item {
    display: flex;
    align-items: center;
    gap: 8px;
    font-weight: 500;
    font-size: 15px;
    line-height: 22px;
    color: var(--ink);
    white-space: nowrap;
  }
  .contact-icon { width: 12px; height: 12px; flex: none; }
  .card-back {
    display: flex;
    align-items: center;
    justify-content: center;
  }
</style>
</head>
<body>
<main class="sheet">
  <section class="card card-front" aria-label="Card front">
    <div class="brand">
      <span class="brand-mark"></span>
      <span class="brand-name">R. Vantello</span>
    </div>
    <span class="tagline-rule"></span>
    <p class="tagline">REAL ESTATE INVESTOR</p>

    <ul class="contact-list">
      <li class="contact-item">
        <svg class="contact-icon" viewBox="0 0 12 12"><rect x="0.75" y="0.75" width="10.5" height="10.5" fill="none" stroke="#cadf82" stroke-width="1.5"/><rect x="4" y="3" width="4" height="6" rx="1" fill="#cadf82"/></svg>
        0456 - 21 38 704
      </li>
      <li class="contact-item">
        <svg class="contact-icon" viewBox="0 0 12 12"><rect x="1" y="4" width="10" height="6" fill="#f78f20"/><rect x="3" y="1" width="6" height="3" fill="#f78f20"/></svg>
        0456 - 21 38 705
      </li>
      <li class="contact-item">
        <svg class="contact-icon" viewBox="0 0 12 12"><rect x="0" y="1" width="12" height="8" fill="#33a6d7"/><rect x="4" y="9" width="4" height="2" fill="#33a6d7"/></svg>
        www.rvantello.com
      </li>
      <li class="contact-item">
        <svg class="contact-icon" viewBox="0 0 12 12"><rect x="0.75" y="2.75" width="10.5" height="7.5" fill="none" stroke="#886aae" stroke-width="1"/><path d="M1 3 L6 7 L11 3" fill="none" stroke="#886aae" stroke-width="1"/></svg>
        info@rvantello.com
      </li>
      <li class="contact-item">
        <svg class="contact-icon" viewBox="0 0 12 12"><rect x="0" y="2" width="12" height="8" fill="#33a6d7"/></svg>
        Linden Lane 14-3
      </li>
      <li class="contact-item">
        <svg class="contact-icon" viewBox="0 0 12 12"><path d="M6 11 C3 7 2 5.5 2 4.2 A4 4 0 0 1 10 4.2 C10 5.5 9 7 6 11 Z" fill="#886aae"/><circle cx="6" cy="4.3" r="1.5" fill="#fff"/></svg>
        54321 Marlowby
      </li>
    </ul>
  </section>

  <section class="card card-back" aria-label="Card back">
    <div class="brand">
      <span class="brand-mark"></span>
      <span class="brand-name">R. Vantello</span>
    </div>
  </section>
</main>
</body>
</html>
```